GUARANTEED WordPress design needed for a sassy, confident charisma coach!

We need a website design for Marla Penrick's brand new, responsive, Wordpress website.
Marla is a trainer / coach who teaches people how to be more charismatic and runs events, publishes video courses and has an ongoing video blog. Her old website is here: www.marlapenrick.co.uk ... but it's now time to have a much better site!
We have a strong idea about the technical components of the website, but we need a designer's eye to create a great style for the site (and provide layered PSD files which our developers will then convert to HTML and CSS).
Marla's brand is sassy, brave, warm and confident. The videos on her existing site give quite a good feel for her personality. We need a clean, stylish and compelling page that isn't too corporate and captures her personality. Every element needs to feel coherent, from fonts and headings to colours and spacing.
The following sites are not exactly what Marla wants (and certainly aren't right in terms of colours) but they give you an idea of the kind of people she is competing against and the area she is operating in:
http://www.tessa-broughley.example/
http://rowanfelsby.example/
Ideally, you will have done something similar and be able to key in on exactly the kind of thing we want: we're not looking to reinvent the wheel. Hopefully you won't mind tweaking a few things if you are close to what we need.
More detail is provided in the word document attached. But in a nutshell we need: a banner, footer, sign-up strap, menu bar, signature and 4 different basic page types. We want bursts of bright colours, contrasted with black and white if possible - sorry we can't be more specific than that...
The word doc also contains some amateur mock-ups as well (the images are also just mockups at this stage) - but although these give a general sense of the structure what we are looking for, we are clearly not designers...so please help! We need a designer's touch!
Kind regards,
Corin
PS The layered PSD versions of the mockup files are available on Cloudvantre: https://files.cloudvantre.example/sh/k72pqa4w1zbtmrd/QXvenlr8Ty3PwMiU6Hs2kYfDb?dl=0
Target Market(s)
Entrepreneurs who need to sell themselves.
Number of Pages Required
4 page

```html
<!DOCTYPE html>
<html lang="en">
<head>
<meta charset="utf-8">
<title>Marla Penrick — Charisma Coach</title>
<link rel="stylesheet" href="https://fonts.googleapis.com/css2?family=Open+Sans:wght@400;600;700;800&family=Gochi+Hand&display=swap">
<style>
:root{
  --red:#f0513c;
  --cyan:#33c6ea;
  --amber:#f4a91d;
  --ink:#222;
  --grey:#777;
  --page:#e9e9e9;
  --white:#fff;
  --btn:#8a8a8a;
}
*{box-sizing:border-box;margin:0;padding:0}
html,body{width:1200px;height:3356px;overflow:hidden}
body{font-family:"Open Sans",Arial,sans-serif;color:var(--ink);background:var(--page);position:relative}
.abs{position:absolute}

/* header */
.site-header{left:0;top:0;width:1200px;height:640px;background:var(--white)}
.main-nav{left:0;top:0;width:1200px;height:48px;display:flex;justify-content:center;gap:20px;align-items:center;font-size:15px;font-weight:600;color:var(--red)}
.main-nav span{display:flex;align-items:center;gap:20px}
.main-nav span+span::before{content:"";width:6px;height:6px;border-radius:50%;background:var(--red);display:inline-block}
.main-nav .current{border-bottom:2px solid var(--red)}
.brand{left:0;top:80px;width:1200px;text-align:center;font-size:52px;font-weight:600;color:var(--ink);letter-spacing:1px}
.hero-photo{left:40px;top:220px;width:520px;height:420px;background:linear-gradient(90deg,#f1ece9 0%,#e7b6ae 45%,#d9473a 70%,#f3efed 100%)}
.tagline{font-family:"Gochi Hand",cursive;font-size:92px;line-height:1;color:var(--ink);font-weight:400}

/* signup strip */
.signup-strip{left:0;top:640px;width:1200px;height:208px;background:var(--cyan)}
.strip-monitor{left:140px;top:30px;width:190px;height:150px;background:linear-gradient(#dfe4e6,#b9c2c6);border-radius:6px}
.strip-copy{left:350px;top:34px;width:620px;font-size:21px;line-height:1.3;color:var(--ink)}
.field{height:40px;background:var(--white);border-radius:20px;font-size:16px;color:var(--grey);padding:9px 18px}
.btn-pill{height:40px;border-radius:20px;background:var(--red);color:var(--white);font-weight:700;font-size:17px;text-align:center;padding:8px 0}
.strip-note{left:350px;top:162px;font-size:14px;font-weight:600}

/* posts */
.post{left:16px;width:764px;background:var(--white)}
.post-banner{left:0;top:0;width:764px;height:420px;color:var(--white);overflow:hidden}
.post-banner h2{position:absolute;left:36px;font-weight:600;font-size:50px;line-height:1.2;text-transform:uppercase;white-space:nowrap}
.post-photo{position:absolute;border-radius:4px}
.post-body{position:absolute;left:40px;width:684px;text-align:center}
.post-body h3{font-size:26px;font-weight:600;margin-bottom:14px}
.post-body p{font-size:16px;line-height:1.5;color:var(--grey)}
.read-more{display:inline-block;margin-top:22px;background:var(--btn);color:var(--white);font-size:15px;padding:8px 22px}

.pager{left:280px;top:2960px;display:flex;gap:14px}
.pager span{width:48px;height:48px;background:var(--white);display:flex;align-items:center;justify-content:center;font-size:18px}
.pager .on{background:var(--red);color:var(--white)}

/* sidebar */
.sidebar{left:800px;width:384px}
.widget-head{height:48px;background:var(--red);color:var(--white);font-size:26px;padding:6px 18px}
.says{top:880px;height:500px;background:var(--white)}
.tab{left:18px;top:60px;color:var(--red);font-weight:700;font-size:18px}
.popular-post{left:18px;width:350px;height:70px;display:flex;gap:14px}
.popular-post .thumb{width:70px;height:64px;background:linear-gradient(#c9b9b0,#8a7d77);flex:none}
.popular-post p{font-size:14px;line-height:1.3;color:#444}
.popular-post b{display:block;font-size:13px;margin-top:4px}
.tags{top:1428px;height:360px;background:var(--white)}
.tag-cloud{left:18px;top:70px;width:350px;display:flex;flex-wrap:wrap;gap:6px}
.tag-cloud span{background:var(--btn);color:var(--white);font-size:13px;padding:3px 8px}
.tag-cloud .l{font-size:26px;font-weight:600}
.tag-cloud .m{font-size:20px;font-weight:600}
.tag-cloud .hot{background:var(--red)}
.promo{top:1820px;height:780px;background:linear-gradient(#5a4c45,#2c2623);color:var(--white);text-align:center}
.promo h4{position:absolute;left:20px;top:20px;width:300px;text-align:left;font-size:36px;line-height:1.15;font-weight:700}
.promo .live{position:absolute;left:0;top:380px;width:384px;font-size:110px;font-weight:800}
.promo .places{position:absolute;left:0;top:520px;width:384px;font-size:34px}
.promo .learn{position:absolute;left:96px;top:630px;width:192px;padding:14px 0;background:var(--cyan);color:var(--ink);font-size:30px;line-height:1.1;font-weight:600}
.dog{top:2640px;height:360px;background:linear-gradient(#f2f2f2,#b9b4b2)}

/* footer */
.footer-signup{left:0;top:3048px;width:1200px;height:172px;background:var(--red);color:var(--white);text-align:center}
.footer-signup p{position:absolute;left:150px;top:24px;width:900px;font-size:20px;line-height:1.35}
.footer-bar{left:0;top:3220px;width:1200px;height:136px;background:var(--white)}
.legal{left:16px;top:20px;font-size:15px;color:var(--red)}
.legal span+span::before{content:"|";color:var(--grey);margin:0 12px}
.copyright{left:16px;top:64px;font-size:13px;color:var(--grey)}
.social-label{left:860px;top:14px;font-size:16px;color:var(--red);font-weight:600}
.social{left:860px;top:44px;display:flex;gap:10px}
.social span{width:34px;height:34px;border-radius:50%;background:#cfcfcf}
</style>
</head>
<body>

<header class="site-header abs">
  <nav class="main-nav abs">
    <span class="current">HOME</span><span>ABOUT US</span><span>EVENTS</span><span>WORK WITH ME</span><span>CORPORATE</span><span>CONTACT US</span>
  </nav>
  <div class="brand abs">Marla Penrick</div>
  <div class="hero-photo abs" role="img" aria-label="Banner photo of Marla in a red dress, seated"></div>
  <div class="tagline abs" style="left:500px;top:240px">Attract</div>
  <div class="tagline abs" style="left:660px;top:370px">Connect</div>
  <div class="tagline abs" style="left:740px;top:500px">Influence</div>
</header>

<section class="signup-strip abs">
  <div class="strip-monitor abs" role="img" aria-label="Computer screen showing the free training video"></div>
  <p class="strip-copy abs">Learn how to unlock the superpower* of your charisma and win all the business you want with this FREE training.</p>
  <div class="field abs" style="left:350px;top:102px;width:220px">First name</div>
  <div class="field abs" style="left:590px;top:102px;width:230px">Email address</div>
  <div class="btn-pill abs" style="left:840px;top:102px;width:180px">YES PLEASE!</div>
  <p class="strip-note abs">* Promise to only use your powers for good</p>
</section>

<article class="post abs" style="top:872px;height:650px">
  <div class="post-banner abs" style="background:var(--red)">
    <h2 style="top:40px">Public speaking...</h2>
    <h2 style="top:170px;font-size:64px;color:var(--ink);text-transform:none">MADE<br>EASY :-)</h2>
    <div class="post-photo" role="img" aria-label="Photo of Marla speaking with a microphone" style="left:500px;top:140px;width:240px;height:280px;background:linear-gradient(#d95a47,#8c2a20)"></div>
  </div>
  <div class="post-body" style="top:446px">
    <h3>Public speaking...made easy</h3>
    <p>Lorem ipsum dolor sit amet, consectetur adipiscing elit. Nam porttitor gravida nisl at mollis. Nulla hendrerit ornare erat a iaculis. Praesent facilisis quam ut velit laoreet ullamcorper. Integer sagittis semper erat scelerisque sagittis. Sed lacus tellus.</p>
    <span class="read-more">Read more</span>
  </div>
</article>

<article class="post abs" style="top:1560px;height:660px">
  <div class="post-banner abs" style="background:var(--cyan)">
    <h2 style="top:40px">Take charge of your<br>style...</h2>
    <h2 style="top:220px">...boost your<br><span style="font-size:64px">confidence</span></h2>
    <div class="post-photo" role="img" aria-label="Photo of Marla in glasses holding a magazine" style="left:530px;top:170px;width:210px;height:250px;background:linear-gradient(#f4c9cf,#5b4a48)"></div>
  </div>
  <div class="post-body" style="top:440px">
    <h3>Take charge of your style...Boost your confidence</h3>
    <p>Lorem ipsum dolor sit amet, consectetur adipiscing elit. Nam porttitor gravida nisl at mollis. Nulla hendrerit ornare erat a iaculis. Praesent facilisis quam ut velit laoreet ullamcorper. Integer sagittis semper erat scelerisque sagittis. Sed lacus tellus.</p>
    <span class="read-more">Read more</span>
  </div>
</article>

<article class="post abs" style="top:2248px;height:692px">
  <div class="post-banner abs" style="background:var(--amber);height:450px">
    <h2 style="top:30px">Unfulfilled? It's<br>time to think<br>about your<br>values...</h2>
    <div class="post-photo" role="img" aria-label="Photo of Marla in a patterned jacket" style="left:530px;top:110px;width:210px;height:200px;background:linear-gradient(#c99656,#5d4a3a)"></div>
    <div class="abs" style="left:0;top:320px;width:764px;height:80px;background:rgba(255,255,255,.55)"></div>
    <h2 style="top:326px;color:var(--ink);font-size:52px">Do this exercise now!</h2>
  </div>
  <div class="post-body" style="top:480px">
    <h3>Unfulfilled? It's time to think about your values...</h3>
    <p>Lorem ipsum dolor sit amet, consectetur adipiscing elit. Nam porttitor gravida nisl at mollis. Nulla hendrerit ornare erat a iaculis. Praesent facilisis quam ut velit laoreet ullamcorper. Integer sagittis semper erat scelerisque sagittis. Sed lacus tellus.</p>
    <span class="read-more">Read more</span>
  </div>
</article>

<div class="pager abs"><span class="on">1</span><span>2</span><span>3</span><span>»</span></div>

<aside class="sidebar says abs">
  <div class="widget-head">Marla Says...</div>
  <div class="tab abs">POPULAR</div>
  <div class="popular-post abs" style="top:96px"><div class="thumb" role="img" aria-label="Post thumbnail"></div><p>Be more dog: 5 lessons we could learn from our best friend<b>13/03/15</b></p></div>
  <div class="popular-post abs" style="top:190px"><div class="thumb" role="img" aria-label="Post thumbnail"></div><p>Are you letting your work bench hold you back?<b>13/03/15</b></p></div>
  <div class="popular-post abs" style="top:284px"><div class="thumb" role="img" aria-label="Post thumbnail"></div><p>How I learned to stop worrying and start NETWORKING<b>13/03/15</b></p></div>
  <div class="popular-post abs" style="top:378px"><div class="thumb" role="img" aria-label="Post thumbnail"></div><p>Simply working from home and other strategies that really work<b>13/03/15</b></p></div>
</aside>

<aside class="sidebar tags abs">
  <div class="widget-head">Tags</div>
  <div class="tag-cloud abs">
    <span class="hot">body language</span><span class="l">capsule wardrobe</span><span>confidence</span><span>handshake</span><span>mindset</span><span>way</span><span>positive</span><span class="m">power pose</span><span>presence</span><span>empower</span><span class="l">rapport</span><span>spring wear</span><span>style</span><span>values</span><span>vision board</span><span>warmth</span>
  </div>
</aside>

<aside class="sidebar promo abs" role="img" aria-label="Event promotion over a photo of a live audience">
  <h4>UNLOCK THE SUPERPOWER OF CHARISMA</h4>
  <div class="live">LIVE</div>
  <div class="places">* Only 6<br>places left.</div>
  <div class="learn">LEARN<br>MORE</div>
</aside>

<aside class="sidebar dog abs" role="img" aria-label="Be More Dog photo of Marla with a dog in a hat"></aside>

<section class="footer-signup abs">
  <p>Hey! Don't go without signing up because you'll miss out on exclusive offers, awesome tips, and weekly motivation in my fab newsletter</p>
  <div class="field abs" style="left:120px;top:112px;width:330px;height:38px;border-radius:19px;text-align:left;padding:7px 18px">First name</div>
  <div class="field abs" style="left:500px;top:112px;width:370px;height:38px;border-radius:19px;text-align:left;padding:7px 18px">Email address</div>
  <div class="btn-pill abs" style="left:910px;top:112px;width:170px;height:38px;background:var(--cyan);color:var(--ink);padding:7px 0">YES PLEASE!</div>
</section>

<footer class="footer-bar abs">
  <div class="legal abs"><span>Privacy Policy</span><span>Term Policy</span><span>Disclaimers</span></div>
  <div class="copyright abs">Copyright © 2016 Marla Penrick Ltd. All Rights Reserved.</div>
  <div class="social-label abs">And that'll make me see</div>
  <div class="social abs"><span></span><span></span><span></span><span></span><span></span><span></span></div>
</footer>

</body>
</html>
```